We are starting a new service that will combine local city menus and specials from local restaurants that will then be emailed and printed out on our website.. its a free service to the subscribers and a small charge to the restaurants. We need something to reflect the restaurant industry and to appeal to the general public alike, free to the end user. They sign up and receive daily specials in an email from our site.. not just one city but any one they pick that we service.. We would need links to include. Home, About Us, Sign Up (for free to public), Add Your Restaurant (increase sales and reduce daily calls).. and Contact Us link.. the name of the service is Town Plates in Motion and website will be townplatesinmotion.example. thank you

```html
<!DOCTYPE html>
<html lang="en">
<head>
<meta charset="utf-8">
<title>Town Plates in Motion</title>
<link rel="stylesheet" href="https://fonts.googleapis.com/css2?family=Alegreya:wght@700&family=Open+Sans:wght@400;600&display=swap">
<style>
  :root {
    --white: #ffffff;
    --accent: #f44b3f;
    --muted: #8a8a8a;
    --hero-red: #b8242a;
    --hero-light: #d9d6d2;
    --hero-dark: #5e5a4e;
  }
  * { margin: 0; padding: 0; box-sizing: border-box; }
  html, body {
    width: 1082px;
    height: 1200px;
    overflow: hidden;
    background: var(--white);
  }
  .page {
    position: relative;
    width: 1082px;
    height: 1200px;
    font-family: "Open Sans", sans-serif;
  }
  .hero {
    position: absolute;
    top: 47px;
    left: 0;
    width: 1082px;
    height: 810px;
    overflow: hidden;
  }
  .hero-backdrop {
    position: absolute;
    inset: 0;
    background:
      radial-gradient(ellipse 260px 380px at 90px 620px, rgba(160,20,25,0.85), transparent 75%),
      radial-gradient(ellipse 200px 520px at 560px 560px, rgba(200,40,45,0.85), transparent 75%),
      radial-gradient(ellipse 420px 300px at 200px 120px, rgba(80,90,60,0.8), transparent 80%),
      radial-gradient(ellipse 300px 240px at 950px 110px, rgba(60,60,55,0.7), transparent 80%),
      linear-gradient(90deg, var(--hero-dark) 0%, var(--hero-red) 25%, var(--hero-light) 45%, var(--hero-red) 55%, var(--hero-light) 75%, #c9c7c4 100%);
  }
  .hero-shade {
    position: absolute;
    inset: 0;
    background: rgba(0,0,0,0.08);
  }
  .hero-title {
    position: absolute;
    top: 200px;
    width: 100%;
    text-align: center;
    font-family: "Alegreya", serif;
    font-weight: 700;
    font-size: 94px;
    line-height: 1;
    color: var(--white);
  }
  .hero-name {
    position: absolute;
    top: 306px;
    width: 100%;
    text-align: center;
    font-family: "Alegreya", serif;
    font-weight: 700;
    font-size: 52px;
    line-height: 1;
    color: var(--white);
  }
  .hero-tagline {
    position: absolute;
    top: 467px;
    width: 100%;
    text-align: center;
    font-size: 40px;
    line-height: 1.2;
    color: var(--white);
    letter-spacing: -0.5px;
  }
  .hero-button {
    position: absolute;
    top: 595px;
    left: 408px;
    width: 271px;
    height: 70px;
    background: var(--accent);
    color: var(--white);
    font-size: 25px;
    line-height: 70px;
    text-align: center;
    text-decoration: none;
    letter-spacing: -0.5px;
  }
  .brand-mark {
    position: absolute;
    top: 1058px;
    width: 100%;
    text-align: center;
    font-size: 26px;
    font-weight: 600;
    color: var(--accent);
  }
  .footer-name {
    position: absolute;
    top: 1152px;
    width: 100%;
    text-align: center;
    font-size: 23px;
    color: var(--muted);
  }
</style>
</head>
<body>
<div class="page">
  <section class="hero">
    <div class="hero-backdrop" role="img" aria-label="Blurred photo of a red and white food truck on a city street"></div>
    <div class="hero-shade"></div>
    <h1 class="hero-title">welcome</h1>
    <h2 class="hero-name">Town Plates in Motion</h2>
    <p class="hero-tagline">Restaurant Specials, Menus and more.</p>
    <a class="hero-button" href="#">LETS EAT LOCAL</a>
  </section>
  <div class="brand-mark">Town Plates in Motion</div>
  <p class="footer-name">Town Plates in Motion</p>
</div>
</body>
</html>
```